Health & Wellness Contest - The Bright Harvest Renewal

We need a postcard design that is professional and grabs the attention of people who see it. The postcard will be left in fitness centers and posted on social media. The front of the card MUST look amazing - make potential participants want to pick it up and find out more information; the back of the card will have the contest details. The goal is to have people sign up for a 90 day fitness program, and most of the marketing will be with this postcard.

Target Market(s)

People that are thinking about beginning a health regiment; people who are already used to exercising and are willing to try a new supplement

Industry/Entity Type

Health And Wellness

Colors

Designer to choose colors to be used in the design.

Requirements
Must have
• Front Cover -- Must have the phrase "The Bright Harvest Renewal" and must have "$2,500 Grand Prize"; and must have "BrightHarvestRenewal.com"
Nice to have
• Design on Front; Details on Back; appeal to both men and women

```html
<!DOCTYPE html>
<html lang="en">
<head>
<meta charset="utf-8">
<title>The Bright Harvest Renewal – Postcard</title>
<link rel="stylesheet" href="https://fonts.googleapis.com/css2?family=Anton&family=Lato:wght@400;700&display=swap">
<style>
  :root{
    --page:#e4e4e4;
    --concrete:#dcdcdc;
    --ink:#111214;
    --navy:#1b3f78;
    --blue:#235196;
    --charcoal:#1d1e20;
    --white:#ffffff;
    --text:#222;
    --stamp:#6e6e6e;
    --rule:#8a8a8a;
  }
  *{margin:0;padding:0;box-sizing:border-box}
  html,body{width:1200px;height:1200px;overflow:hidden;background:var(--page)}
  .postcard{position:absolute;left:274px;width:656px;height:508px;overflow:hidden;box-shadow:0 8px 18px rgba(0,0,0,.25)}
  .postcard--front{top:45px;background:var(--concrete)}
  .postcard--back{top:627px;background:var(--white)}
  .backdrop{position:absolute;inset:0}
  .abs{position:absolute}

  /* front */
  .sponsor{left:100px;top:44px;display:flex;align-items:center;gap:5px;font:700 11px/1 "Lato",sans-serif;letter-spacing:.6px;color:var(--navy);white-space:nowrap}
  .sponsor__mark{width:10px;height:10px;background:var(--navy)}
  .title-side{left:38px;top:290px;transform-origin:0 0;transform:rotate(-90deg);font:400 60px/1 "Anton",sans-serif;color:var(--navy);letter-spacing:1px}
  .title{left:112px;top:78px;font-family:"Anton",sans-serif;text-transform:uppercase;line-height:.98}
  .title__the{display:block;font-size:78px;color:var(--ink)}
  .title__bright{display:block;font-size:40px;color:var(--navy);letter-spacing:1px}
  .title__harvest{display:block;font-size:60px;color:var(--ink)}
  .prize{left:40px;top:308px;width:320px;height:46px;background:var(--ink);color:var(--white);font:400 30px/46px "Anton",sans-serif;text-align:center;letter-spacing:1px}
  .details{left:54px;top:372px;font:400 15px/1.35 "Lato",sans-serif;color:var(--text)}
  .site{left:116px;top:470px;font:400 16px/1 "Lato",sans-serif;color:var(--white);letter-spacing:.3px}

  /* back */
  .program{left:22px;top:207px;transform-origin:0 0;transform:rotate(-90deg);font:400 30px/1 "Anton",sans-serif;color:var(--navy);letter-spacing:1px}
  .signup{left:58px;top:64px;font:400 32px/1.08 "Anton",sans-serif;text-transform:uppercase;color:var(--navy)}
  .signup span{display:block}
  .signup .signup__dark{color:var(--ink)}
  .mission{left:20px;top:228px;width:210px;font:400 12.5px/1.4 "Lato",sans-serif;color:var(--text)}
  .divider{left:20px;top:288px;width:275px;height:1px;background:var(--rule)}
  .invite{left:18px;top:296px;width:300px;font:400 12.5px/1.25 "Lato",sans-serif;color:var(--text)}
  .benefits{top:352px;list-style:none;font:400 12.5px/15.5px "Lato",sans-serif;color:var(--text)}
  .benefits li::before{content:"";display:inline-block;width:8px;height:8px;border-radius:50%;background:var(--navy);margin-right:5px}
  .benefits--a{left:18px}
  .benefits--b{left:170px}
  .benefits-rule{left:160px;top:350px;width:1px;height:70px;background:var(--ink)}
  .deadline{left:40px;top:464px;width:240px;text-align:center;font:400 13px/1.35 "Lato",sans-serif;color:var(--white)}
  .stamp{left:533px;top:69px;width:76px;height:82px;background:var(--stamp)}
  .address-line{left:408px;width:209px;height:1px;background:var(--rule)}
</style>
</head>
<body>

<section class="postcard postcard--front">
  <svg class="backdrop" viewBox="0 0 656 508" width="656" height="508">
    <defs>
      <linearGradient id="photoFront" x1="0" y1="0" x2="1" y2="1">
        <stop offset="0" stop-color="#2a2c30"/>
        <stop offset=".5" stop-color="#7a4a32"/>
        <stop offset="1" stop-color="#1a1b1d"/>
      </linearGradient>
    </defs>
    <polygon points="268,0 300,0 488,508 448,508" fill="var(--navy)"/>
    <polygon points="300,0 656,0 656,508 488,508" fill="var(--charcoal)"/>
    <g role="img" aria-label="Photo of a fit woman in black sportswear holding dumbbells, blue smoke behind her">
      <polygon points="380,40 600,40 620,508 430,508 380,200" fill="url(#photoFront)" opacity=".9"/>
    </g>
    <polygon points="0,492 420,410 470,430 488,508 0,508" fill="var(--blue)"/>
    <polygon points="0,488 420,406 440,416 0,498" fill="var(--ink)"/>
    <polygon points="20,296 40,296 40,354 20,354 8,325" fill="var(--blue)"/>
    <polygon points="360,296 382,296 370,325 382,354 360,354" fill="var(--blue)"/>
  </svg>

  <div class="abs sponsor"><span class="sponsor__mark"></span>NORTHGATE LAW GROUP</div>
  <div class="abs title-side">Renewal</div>
  <h1 class="abs title">
    <span class="title__the">The</span>
    <span class="title__bright">Bright</span>
    <span class="title__harvest">Harvest</span>
  </h1>
  <div class="abs prize">"$2,500 GRAND PRIZE</div>
  <p class="abs details">For Challenge details, email one of our<br>sponsors at Info@NorthgateLaw.org.</p>
  <p class="abs site">BrightHarvestRenewal.com</p>
</section>

<section class="postcard postcard--back">
  <svg class="backdrop" viewBox="0 0 656 508" width="656" height="508">
    <defs>
      <linearGradient id="photoBack" x1="0" y1="0" x2="0" y2="1">
        <stop offset="0" stop-color="#8a5a3e"/>
        <stop offset=".7" stop-color="#3a3b3e"/>
        <stop offset="1" stop-color="#ffffff"/>
      </linearGradient>
    </defs>
    <polygon points="103,0 408,0 385,140 210,110" fill="var(--charcoal)"/>
    <polygon points="103,0 125,0 240,110 210,110" fill="var(--navy)"/>
    <polygon points="408,0 418,0 327,508 317,508" fill="var(--navy)"/>
    <g role="img" aria-label="Photo of a fit man and woman in black workout tops">
      <polygon points="240,40 400,15 390,200 385,222 240,222" fill="url(#photoBack)"/>
    </g>
    <polygon points="0,456 340,406 317,508 0,508" fill="var(--blue)"/>
    <polygon points="0,452 335,400 333,408 0,460" fill="var(--ink)"/>
  </svg>

  <div class="abs program">PROGRAM</div>
  <h2 class="abs signup">
    <span>Sign Up</span>
    <span>For A</span>
    <span>90 Days</span>
    <span class="signup__dark">Fitness</span>
  </h2>
  <p class="abs mission">The Bright Harvest Renewal has one mission – to help people be a better version of themselves.</p>
  <div class="abs divider"></div>
  <p class="abs invite">Join us in the Bright Harvest Renewal and experience some of the benefits that countless others have seen:</p>
  <ul class="abs benefits benefits--a">
    <li>Better health</li>
    <li>Appetite suppression</li>
    <li>Better energy</li>
    <li>Fat Loss</li>
    <li>Better focus</li>
  </ul>
  <div class="abs benefits-rule"></div>
  <ul class="abs benefits benefits--b">
    <li>Increased awareness</li>
    <li>Better mood</li>
    <li>Muscle preservation</li>
    <li>Better sleep</li>
  </ul>
  <p class="abs deadline">Challenge Deadline:<br>Register by October 31, 2017.</p>

  <div class="abs stamp"></div>
  <div class="abs address-line" style="top:270px"></div>
  <div class="abs address-line" style="top:315px"></div>
  <div class="abs address-line" style="top:365px"></div>
</section>

</body>
</html>
```